HVAC Technical Manual Covers for Duct Design, Load Calculation and Equipment Selection

I work for an HVAC trade association that publishes technical manuals. We have a series of books that need new covers since there have been many changes.

I'd like the books to have a similar style to each other (like the current Manual W and T, see below). Here is a listing of all our current manuals https://www.oplxguild.org/standards/technical-manuals. We plan on updating more in the future, like K, , P and XB. So I'd like a design that we can continue on.

The 3 covers I need are
1. Manual Q Residential Load Calculation
https://www.oplxguild.org/standards/technical-manuals/manual-q
2. Manual T® - Residential Duct Systems
https://www.oplxguild.org/standards/technical-manuals/manual-t
3. Manual W® - Residential Equipment Selection
https://www.oplxguild.org/standards/technical-manuals/manual-w

I included our logos and style guide as a resource. But I'm open to all images and colors. The audience is primarily engineers, software developers, code officials and HVAC technicians. These 3 manuals are aimed at residential (single-family homes/townhomes) in the United States.

Target Market(s)

The audience is primarily engineers, software developers, code officials and HVAC technicians.

Industry/Entity Type

HVACR, Air Conditioning

Font styles to use
Sans Serif

Requirements
Must have
• OPLX Logo, manual letter and full title. Single Family or townhome images
Should not have
• commercial buildings, mini splits, hardhats

```html
<!DOCTYPE html>
<html lang="en">
<head>
<meta charset="utf-8">
<title>OPLX Technical Manual Covers</title>
<link href="https://fonts.googleapis.com/css2?family=Arimo:wght@400;700&display=swap" rel="stylesheet">
<style>
  :root {
    --page: #f3f3f3;
    --white: #ffffff;
    --ink-grey: #a7a7a7;
    --swatch-sage: #e6e9dd;
    --swatch-grey: #b9babc;
    --logo-blue: #2b6cb3;
    --load-orange: #ef7d3a;
    --duct-blue: #4b6fa6;
    --equip-sky: #74c6ea;
  }
  * { margin: 0; padding: 0; box-sizing: border-box; }
  html, body { width: 1200px; height: 2701px; overflow: hidden; background: var(--page); }
  body { font-family: "Arimo", Arial, sans-serif; position: relative; }

  .cover-slot { position: absolute; left: 0; width: 1200px; height: 900px; }
  .cover-slot--load { top: 0; }
  .cover-slot--duct { top: 900px; }
  .cover-slot--equipment { top: 1800px; }

  .cover {
    position: absolute; left: 280px; top: 130px;
    width: 640px; height: 640px;
    background: var(--white);
    box-shadow: 0 18px 40px rgba(0,0,0,0.12);
    overflow: hidden;
  }
  .cover--load { --accent: var(--load-orange); --letter-size: 250px; }
  .cover--duct { --accent: var(--duct-blue); --letter-size: 270px; }
  .cover--equipment { --accent: var(--equip-sky); --letter-size: 210px; }

  .masthead { position: absolute; left: 40px; top: 40px; display: flex; align-items: center; gap: 18px; }
  .publisher-mark { display: flex; align-items: center; gap: 8px; }
  .publisher-mark__square { width: 22px; height: 22px; background: var(--logo-blue); }
  .publisher-mark__name { font-size: 34px; font-weight: 400; color: var(--logo-blue); letter-spacing: 1px; }
  .partner-badge { width: 96px; height: 40px; border-radius: 50%; background: #e8edf4; }

  .accent-band { position: absolute; left: 40px; right: 0; top: 112px; height: 22px; background: var(--accent); }

  .cover-photo { position: absolute; left: 40px; right: 0; top: 134px; height: 236px; }
  .cover--load .cover-photo { background: linear-gradient(120deg, #d9c7a3 0%, #9a7b60 40%, #5a4a43 70%, #b49a82 100%); }
  .cover--duct .cover-photo { background: linear-gradient(180deg, #c9cde6 0%, #8e96c4 40%, #5b6491 70%, #b0b6cf 100%); }
  .cover--equipment .cover-photo { background: linear-gradient(180deg, #8fd0ef 0%, #c4e6f5 40%, #e9e0cc 70%, #7c9a5c 100%); }

  .manual-letter {
    position: absolute; left: 445px; width: 185px; top: 250px; height: 275px;
    display: flex; align-items: flex-end; justify-content: center;
    font-size: var(--letter-size); font-weight: 700; line-height: 0.8; color: var(--accent);
  }

  .cover-text { position: absolute; left: 130px; top: 400px; width: 300px; }
  .cover-title { font-size: 30px; font-weight: 700; line-height: 1.05; color: var(--accent); }
  .cover-author { margin-top: 6px; font-size: 15px; color: var(--ink-grey); }
  .cover-manual { margin-top: 14px; font-size: 22px; color: var(--accent); }
  .cover-subtitle { margin-top: 3px; font-size: 10px; line-height: 1.4; color: var(--accent); }

  .footer-bar { position: absolute; left: 130px; width: 320px; top: 590px; height: 20px; background: var(--accent); }
  .swatch { position: absolute; height: 22px; }
  .swatch--sage { left: 462px; width: 96px; top: 560px; background: var(--swatch-sage); }
  .swatch--grey { left: 568px; width: 72px; top: 536px; background: var(--swatch-grey); }

  .signoff { position: absolute; right: 70px; top: 2575px; text-align: center; }
  .signoff__name { font-size: 40px; color: var(--logo-blue); letter-spacing: 1px; }
  .signoff__tagline { font-size: 10px; color: var(--logo-blue); }
</style>
</head>
<body>

<section class="cover-slot cover-slot--load">
  <article class="cover cover--load">
    <header class="masthead">
      <div class="publisher-mark"><span class="publisher-mark__square"></span><span class="publisher-mark__name">OPLX</span></div>
      <div class="partner-badge"></div>
    </header>
    <div class="accent-band"></div>
    <div class="cover-photo" role="img" aria-label="Family relaxing on a sofa at home"></div>
    <div class="manual-letter">Q</div>
    <div class="cover-text">
      <h1 class="cover-title">Residential Load Calculation</h1>
      <p class="cover-author">Dale Morrow, P.E.</p>
      <p class="cover-manual">Manual Q</p>
      <p class="cover-subtitle">(8th Edition - Full) [NSB/OPLX 2 Manual Q - 2016]</p>
    </div>
    <div class="footer-bar"></div>
    <div class="swatch swatch--sage"></div>
    <div class="swatch swatch--grey"></div>
  </article>
</section>

<section class="cover-slot cover-slot--duct">
  <article class="cover cover--duct">
    <header class="masthead">
      <div class="publisher-mark"><span class="publisher-mark__square"></span><span class="publisher-mark__name">OPLX</span></div>
      <div class="partner-badge"></div>
    </header>
    <div class="accent-band"></div>
    <div class="cover-photo" role="img" aria-label="Single-family house at dusk with lit windows"></div>
    <div class="manual-letter">T</div>
    <div class="cover-text">
      <h1 class="cover-title">Residential Duck System</h1>
      <p class="cover-author">Dale Morrow, P.E.</p>
      <p class="cover-manual">Manual T</p>
      <p class="cover-subtitle">Systems and Applications | Blowers and Air-side Devices | Sizing Calculators | Efficiency, Leakage and Noise</p>
    </div>
    <div class="footer-bar"></div>
    <div class="swatch swatch--sage"></div>
    <div class="swatch swatch--grey"></div>
  </article>
</section>

<section class="cover-slot cover-slot--equipment">
  <article class="cover cover--equipment">
    <header class="masthead">
      <div class="publisher-mark"><span class="publisher-mark__square"></span><span class="publisher-mark__name">OPLX</span></div>
      <div class="partner-badge"></div>
    </header>
    <div class="accent-band"></div>
    <div class="cover-photo" role="img" aria-label="Large family home under a clear blue sky"></div>
    <div class="manual-letter">W</div>
    <div class="cover-text">
      <h1 class="cover-title">Residential Equipment Selection</h1>
      <p class="cover-author">Dale Morrow, P.E.</p>
      <p class="cover-manual">Manual W</p>
      <p class="cover-subtitle">Air Conditioners | Heat Pump | Mini Splits | Condenser | Geothermal | Boiler | Furnace</p>
    </div>
    <div class="footer-bar"></div>
    <div class="swatch swatch--sage"></div>
    <div class="swatch swatch--grey"></div>
  </article>
</section>

<footer class="signoff">
  <div class="signoff__name">OPLX</div>
  <div class="signoff__tagline">Open Plant Layout Exchange</div>
</footer>

</body>
</html>
```